I would like a single page website for Skylark Rentals Australia. In the file list provided there is basic information to be included as well as our logo with colors, fonts and images to be included.
Site must be very simple and be able to be loaded onto smart phones etc very quickly.
Site needs to be very smart in appearance

Target Market(s)

All prospective drone customers from Police to Parties.

Industry/Entity Type

Hire

Coding

Coded - Design and coding required

Number of Pages Required

1 page

Requirements
Must have
• Must have variation of color schemes supplied
Nice to have
• Must be very eye catching without going over the top
Should not have
• Anything slow to load.

```html
<!DOCTYPE html>
<html lang="en">
<head>
<meta charset="utf-8">
<title>Skylark Rentals Australia</title>
<link href="https://fonts.googleapis.com/css2?family=Lato:ital,wght@0,400;0,700;1,400&family=Oswald:wght@400&display=swap" rel="stylesheet">
<style>
:root{
  --green:#6dbb4f;
  --dark:#2b2b2b;
  --text:#3a3a3a;
  --muted:#8a8a8a;
  --panel:#f2f2f2;
  --rule:#d6d6d6;
  --footer:#7b7b7d;
  --social:#555555;
  --link:#3b5f8a;
}
*{box-sizing:border-box;margin:0;padding:0}
html,body{width:937px;height:1200px;overflow:hidden;background:#fff}
body{font-family:'Lato',sans-serif;color:var(--text)}
.page{position:relative;width:937px;height:1200px;overflow:hidden;border-top:2px solid #bdbdbd}
.abs{position:absolute}

/* header */
.brand{left:104px;top:30px;display:flex;align-items:center;gap:12px}
.brand-mark{width:22px;height:22px;border-radius:50%;background:var(--green)}
.brand-name{font-size:27px;font-weight:700;color:var(--green);line-height:1.1;letter-spacing:.5px}
.brand-name span{display:block}
.social{right:103px;top:7px;display:flex;gap:8px}
.social i{display:block;width:22px;height:22px;border-radius:50%;background:var(--social)}
.social i:first-child{background:var(--green)}
.contact{right:103px;top:46px;text-align:right}
.contact-name{font-size:18px;font-weight:700;color:var(--green);letter-spacing:.3px;line-height:22px}
.contact-row{display:flex;justify-content:flex-end;align-items:center;gap:5px;color:var(--dark);font-weight:700}
.contact-phone{font-size:16px;margin-top:1px}
.contact-mail{font-size:11.5px;margin-top:4px}

/* hero */
.hero{left:0;top:115px;width:937px;height:368px;background:linear-gradient(180deg,#c5c9ce 0%,#b7bcc2 45%,#a7aaa8 78%,#c9beac 90%,#b9ad98 100%)}
.hero-title{left:102px;top:175px;font-family:'Oswald',sans-serif;font-size:30px;line-height:40px;color:var(--dark);text-transform:uppercase}
.hero-title .sub{display:block;margin-top:6px;margin-left:4px}
.dots{left:102px;top:335px;display:flex;gap:7px}
.dots i{width:11px;height:11px;border-radius:50%;background:#fff}
.dots i:first-child{background:#3c5a88;border:1px solid #fff}

/* features */
.feature{top:518px;width:180px;text-align:center}
.feature svg{display:block;margin:0 auto}
.feature h3{margin-top:20px;font-size:16px;font-weight:700;line-height:19px;color:var(--dark);text-transform:uppercase}

/* panel */
.panel{left:0;top:707px;width:937px;height:228px;background:var(--panel);border-top:1px solid #e2e2e2;border-bottom:1px solid #e2e2e2}
.sec-head{font-size:18px;font-weight:700;color:var(--dark);text-transform:uppercase;line-height:22px}
.sec-head em{font-style:normal;color:var(--green)}
.sec-rule{height:1px;background:var(--rule);position:relative;margin-top:8px}
.sec-rule::before{content:"";position:absolute;left:0;top:-1px;width:54px;height:2px;background:#b8b8b8}
.about{left:102px;top:721px;width:415px}
.about p{font-size:10.4px;line-height:14.4px;color:#2e2e2e;margin-top:10px}
.about p + p{margin-top:8px}
.read-more{display:inline-block;margin-top:9px;margin-left:2px;font-size:11px;font-style:italic;color:var(--link);text-decoration:none}
.read-more b{color:#4aa3d8;font-style:normal}
.divider{left:546px;top:735px;width:1px;height:160px;background:#e0e0e0}
.inquiry{left:579px;top:721px;width:255px}
.inquiry form{margin-top:14px}
.field{display:block;width:255px;height:20px;border:1px solid #c8c8c8;background:#fff;font:10px 'Lato',sans-serif;color:#333;padding:0 5px;margin-bottom:6px}
textarea.field{height:44px;padding-top:4px;resize:none}
.submit{display:block;margin-left:auto;width:66px;height:18px;border:0;background:var(--green);color:#fff;font:700 12px 'Lato',sans-serif;letter-spacing:.3px}

/* serve */
.serve-head{left:104px;top:960px;width:728px;text-align:center}
.serve-head h2{font-size:19px;font-weight:700;color:var(--dark);letter-spacing:.3px}
.serve-rule{height:1px;background:var(--rule);margin-top:6px;position:relative}
.serve-rule::before{content:"";position:absolute;left:321px;top:-1px;width:98px;height:2px;background:#b8b8b8}
.serve-item{display:flex;gap:6px;align-items:flex-start;font-size:11px;line-height:14.5px;color:var(--muted);letter-spacing:.2px}
.serve-item svg{flex:none;margin-top:-1px}

/* footer */
.footer{left:0;top:1170px;width:937px;height:30px;background:var(--footer);color:#fff;font-size:11px;text-align:center;line-height:30px}
</style>
</head>
<body>
<div class="page">

  <header>
    <div class="abs brand">
      <div class="brand-mark"></div>
      <div class="brand-name"><span>SKYLARK RENTALS</span><span>AUSTRALIA</span></div>
    </div>
    <div class="abs social" aria-label="Social links"><i></i><i></i><i></i><i></i></div>
    <div class="abs contact">
      <div class="contact-name">SAM WHITFORD</div>
      <div class="contact-row contact-phone">
        <svg width="16" height="16" viewBox="0 0 16 16" aria-hidden="true"><circle cx="8" cy="8" r="7" fill="none" stroke="#2b2b2b" stroke-width="1.4"/><path d="M5.6 4.3l1.3 1.6-.7.9c.4 1 1.2 1.9 2.2 2.4l.9-.7 1.6 1.3-.8 1.2C7.3 10.800 4.800 8.200 4.400 5.100z" fill="#2b2b2b"/></svg>
        123-555-0142
      </div>
      <div class="contact-row contact-mail">
        <svg width="17" height="17" viewBox="0 0 17 17" aria-hidden="true"><circle cx="8.5" cy="8.5" r="7.6" fill="none" stroke="#2b2b2b" stroke-width="1.2"/><rect x="4.5" y="5.8" width="8" height="5.5" fill="#2b2b2b"/><path d="M4.5 5.8l4 3 4-3" fill="none" stroke="#fff" stroke-width=".9"/></svg>
        hello@skylarkrentals.com.au
      </div>
    </div>
  </header>

  <section class="abs hero" role="img" aria-label="Photo of a white camera drone flying over a beach construction site with workers and an excavator"></section>
  <h1 class="abs hero-title">Our customers range from<br>police to parties<span class="sub">4K video footage, 12MP images</span></h1>
  <div class="abs dots"><i></i><i></i><i></i><i></i></div>

  <section class="features">
    <div class="abs feature" style="left:76px">
      <svg width="104" height="104" viewBox="0 0 104 104" aria-hidden="true"><circle cx="52" cy="52" r="50" fill="#fff" stroke="#6dbb4f" stroke-width="3"/><circle cx="52" cy="52" r="45" fill="#6dbb4f"/><path d="M52 27l19 7v16c0 13-8 22-19 27-11-5-19-14-19-27V34z" fill="#fff"/><path d="M44 52l6 6 11-12" fill="none" stroke="#6dbb4f" stroke-width="4"/></svg>
      <h3>CASA Endorsed<br>Pilot</h3>
    </div>
    <div class="abs feature" style="left:281px">
      <svg width="104" height="104" viewBox="0 0 104 104" aria-hidden="true"><circle cx="52" cy="52" r="50" fill="#fff" stroke="#6dbb4f" stroke-width="3"/><circle cx="52" cy="52" r="45" fill="#6dbb4f"/><path d="M26 52a26 22 0 0 1 52 0c-4-3-8-3-13 0-4-3-9-3-13 0-4-3-9-3-13 0-5-3-9-3-13 0z" fill="#fff"/><path d="M52 52v18a5 5 0 0 1-10 0" fill="none" stroke="#fff" stroke-width="4"/></svg>
      <h3>Full Public Liability<br>Insurance</h3>
    </div>
    <div class="abs feature" style="left:474px">
      <svg width="104" height="104" viewBox="0 0 104 104" aria-hidden="true"><circle cx="52" cy="52" r="50" fill="#fff" stroke="#6dbb4f" stroke-width="3"/><circle cx="52" cy="52" r="45" fill="#6dbb4f"/><path d="M37 27h22l10 10v40H37z" fill="#fff"/><path d="M44 45h18M44 53h18M44 61h12" stroke="#6dbb4f" stroke-width="3"/></svg>
      <h3>All Operating<br>Licences</h3>
    </div>
    <div class="abs feature" style="left:666px">
      <svg width="104" height="104" viewBox="0 0 104 104" aria-hidden="true"><circle cx="52" cy="52" r="50" fill="#fff" stroke="#6dbb4f" stroke-width="3"/><circle cx="52" cy="52" r="45" fill="#6dbb4f"/><circle cx="52" cy="52" r="26" fill="none" stroke="#fff" stroke-width="7"/><path d="M40 50l10 11 24-27" fill="none" stroke="#fff" stroke-width="8" stroke-linecap="round" stroke-linejoin="round"/><path d="M40 50l10 11 24-27" fill="none" stroke="#6dbb4f" stroke-width="3" stroke-linecap="round" stroke-linejoin="round" opacity="0"/></svg>
      <h3>CASA Compliance<br>Standards</h3>
    </div>
  </section>

  <section class="abs panel"></section>
  <div class="abs about">
    <h2 class="sec-head">About <em>Skylark Rentals Australia</em></h2>
    <div class="sec-rule"></div>
    <p>Lorem ipsum dolor sit amet, consectetur adipiscing elit. Aenean et dignissim sem, interdum risus. Vestibulum consectetur nisi mollis diam pulvinar adipiscing. Vestibulum ut urna nec nibh adipiscing facilisis. Etiam auctor porta lacus ac luctus. Praesent ac libero fermentum, rhoncus magna a, dapibus mauris. Nam ut auctor justo. Sed ante odio, luctus quis nequ nec, adipiscing eleifend arcu. Integer nunc turpis, porttitor at lorem ut.</p>
    <p>Quisque hendrerit molestie commodo. Aliquam imperdiet varius tortor ut condiment Nulla ornare ultricies nunc et scelerisque. Class aptent taciti sociosqu ad litora torquent conubia nostra, per inceptos himenaeos. Mauris mattis ultrices diam nec luctus.</p>
    <a class="read-more" href="#">Read More <b>»</b></a>
  </div>
  <div class="abs divider"></div>
  <div class="abs inquiry">
    <h2 class="sec-head">Quick <em>Inquiry</em></h2>
    <div class="sec-rule"></div>
    <form>
      <input class="field" type="text" placeholder="Your Name">
      <input class="field" type="email" placeholder="Email">
      <input class="field" type="tel" placeholder="Phone">
      <textarea class="field" placeholder="Message"></textarea>
      <button class="submit" type="button">SUBMIT</button>
    </form>
  </div>

  <div class="abs serve-head">
    <h2>WE SERVE</h2>
    <div class="serve-rule"></div>
  </div>

  <div class="abs serve-item" style="left:102px;top:1015px"><svg width="16" height="22" viewBox="0 0 16 22"><path d="M1 5h9v15H1z" fill="none" stroke="#9a9a9a"/><path d="M3 11l3 6 9-16" fill="none" stroke="#9a9a9a" stroke-width="1.2"/></svg><span>Special Occasions, Children’s<br>Birthday Parties, Weddings</span></div>
  <div class="abs serve-item" style="left:375px;top:1015px"><svg width="16" height="22" viewBox="0 0 16 22"><path d="M1 5h9v15H1z" fill="none" stroke="#9a9a9a"/><path d="M3 11l3 6 9-16" fill="none" stroke="#9a9a9a" stroke-width="1.2"/></svg><span>Sporting events -4K Video of<br>yourself participating in marathons</span></div>
  <div class="abs serve-item" style="left:675px;top:1015px"><svg width="16" height="22" viewBox="0 0 16 22"><path d="M1 5h9v15H1z" fill="none" stroke="#9a9a9a"/><path d="M3 11l3 6 9-16" fill="none" stroke="#9a9a9a" stroke-width="1.2"/></svg><span style="margin-top:7px">Real Estate Brochures</span></div>

  <div class="abs serve-item" style="left:102px;top:1062px"><svg width="16" height="22" viewBox="0 0 16 22"><path d="M1 5h9v15H1z" fill="none" stroke="#9a9a9a"/><path d="M3 11l3 6 9-16" fill="none" stroke="#9a9a9a" stroke-width="1.2"/></svg><span>Construction Project Updates<br>For Remote Stake Holders</span></div>
  <div class="abs serve-item" style="left:375px;top:1062px"><svg width="16" height="22" viewBox="0 0 16 22"><path d="M1 5h9v15H1z" fill="none" stroke="#9a9a9a"/><path d="M3 11l3 6 9-16" fill="none" stroke="#9a9a9a" stroke-width="1.2"/></svg><span>Surveillance – Police, Local<br>councils worksafe etc</span></div>
  <div class="abs serve-item" style="left:675px;top:1062px"><svg width="16" height="22" viewBox="0 0 16 22"><path d="M1 5h9v15H1z" fill="none" stroke="#9a9a9a"/><path d="M3 11l3 6 9-16" fill="none" stroke="#9a9a9a" stroke-width="1.2"/></svg><span>Building/Roof Condition<br>Inspections</span></div>

  <div class="abs serve-item" style="left:102px;top:1108px"><svg width="16" height="22" viewBox="0 0 16 22"><path d="M1 5h9v15H1z" fill="none" stroke="#9a9a9a"/><path d="M3 11l3 6 9-16" fill="none" stroke="#9a9a9a" stroke-width="1.2"/></svg><span style="margin-top:7px">Lost Pets</span></div>
  <div class="abs serve-item" style="left:375px;top:1108px"><svg width="16" height="22" viewBox="0 0 16 22"><path d="M1 5h9v15H1z" fill="none" stroke="#9a9a9a"/><path d="M3 11l3 6 9-16" fill="none" stroke="#9a9a9a" stroke-width="1.2"/></svg><span style="margin-top:7px">Accident Reconstructions</span></div>
  <div class="abs serve-item" style="left:675px;top:1108px"><svg width="16" height="22" viewBox="0 0 16 22"><path d="M1 5h9v15H1z" fill="none" stroke="#9a9a9a"/><path d="M3 11l3 6 9-16" fill="none" stroke="#9a9a9a" stroke-width="1.2"/></svg><span style="margin-top:7px">Insurance Assessing</span></div>

  <footer class="abs footer">Copyright 2015 SkylarkRentalsAustralia. All Rights Reserved</footer>
</div>
</body>
</html>
```